Business card for a "family office" company

Please provide professional looking business card designs, incorporating the attached logo and below details. Harrowmere Holdings Pty Ltd is a family office / financial investment company. We are looking for a modern, professional and contemporary card design.

Industry/Entity Type

Finance

Contact Information for Business Card

Name: Dean Mollick
Title: Director
Company: Harrowmere Holdings Pty Ltd
Email: harrowdean@quillnet.example
Mobile: 0462 735 418
Address: 4/312 Barnaby Parade, Cottesloe WA 6011, Australia

Requirements
Must have
• All details above and the logo. logo only on back side. incorporate colours of logo
Nice to have
• up to you
Should not have
• ?

```html
<!DOCTYPE html>
<html lang="en">
<head>
<meta charset="utf-8">
<title>Harrowmere Holdings – Business Card</title>
<link href="https://fonts.googleapis.com/css2?family=Open+Sans:wght@400;600;700&display=swap" rel="stylesheet">
<style>
  :root {
    --backdrop: #0d0d0d;
    --paper: #faf7f2;
    --navy: #25215a;
    --royal: #2e3c8e;
    --white: #ffffff;
    --ink: #1c1a44;
  }
  * { margin: 0; padding: 0; box-sizing: border-box; }
  html, body {
    width: 1200px; height: 1000px; overflow: hidden;
    background: var(--backdrop);
    font-family: "Open Sans", sans-serif;
  }
  .stage { position: relative; width: 1200px; height: 1000px; }
  .card {
    position: absolute; top: 350px;
    width: 525px; height: 300px;
    background: var(--paper);
    overflow: hidden;
    box-shadow: 0 6px 18px rgba(0,0,0,.6);
  }
  .card-back { left: 50px; }
  .card-front { left: 625px; }

  /* back side: brand */
  .brand {
    position: absolute; inset: 0;
    display: flex; align-items: center; justify-content: center; gap: 14px;
  }
  .brand-square { width: 30px; height: 30px; background: var(--navy); }
  .brand-name {
    font-weight: 600; font-size: 30px; color: var(--navy); letter-spacing: 1px;
  }

  /* front side: details */
  .person { position: absolute; left: 26px; top: 12px; color: var(--ink); }
  .person-name { font-weight: 700; font-size: 19px; line-height: 1.15; }
  .person-title { font-size: 14px; line-height: 1.2; }

  .company-band {
    position: absolute; left: 0; top: 66px; width: 72%; height: 50px;
    background: var(--royal);
    color: var(--white); font-size: 20px;
    display: flex; align-items: center; padding-left: 26px;
  }
  .lower-panel-left {
    position: absolute; left: 0; top: 124px; width: 72%; height: 60px;
    background: var(--navy);
  }
  .lower-panel {
    position: absolute; left: 0; top: 184px; width: 100%; bottom: 0;
    background: var(--navy);
  }
  .accent-block {
    position: absolute; right: 0; top: 132px; width: 13%; height: 42px;
    background: var(--royal);
  }

  .contacts {
    position: absolute; left: 26px; top: 134px;
    list-style: none; color: var(--white); font-size: 13px;
  }
  .contacts li { display: flex; align-items: center; gap: 9px; line-height: 22px; }
  .contacts svg { width: 13px; height: 13px; flex: none; }

  .address {
    position: absolute; right: 28px; bottom: 22px;
    color: var(--white); font-size: 15px; text-align: right; line-height: 1.35;
  }
</style>
</head>
<body>
<main class="stage">
  <section class="card card-back" aria-label="Card back">
    <div class="brand">
      <span class="brand-square"></span>
      <span class="brand-name">Harrowmere Holdings</span>
    </div>
  </section>

  <section class="card card-front" aria-label="Card front">
    <div class="person">
      <p class="person-name">Dean Mollick</p>
      <p class="person-title">Director</p>
    </div>
    <div class="company-band">Harrowmere Holdings Pty Ltd</div>
    <div class="lower-panel-left"></div>
    <div class="lower-panel"></div>
    <div class="accent-block"></div>

    <ul class="contacts">
      <li>
        <svg viewBox="0 0 16 16" fill="none" stroke="#fff" stroke-width="1.5"><rect x="4" y="1" width="8" height="14" rx="1.5"/><line x1="7" y1="12.5" x2="9" y2="12.5"/></svg>
        0462 735 418
      </li>
      <li>
        <svg viewBox="0 0 16 16" fill="#fff"><path d="M1 3h14v10H1z"/><path d="M1 3l7 6 7-6" stroke="#25215a" stroke-width="1.3" fill="none"/></svg>
        harrowdean@quillnet.example
      </li>
      <li>
        <svg viewBox="0 0 16 16" fill="none" stroke="#fff" stroke-width="1.3"><circle cx="8" cy="8" r="6.5"/><ellipse cx="8" cy="8" rx="3" ry="6.5"/><line x1="1.5" y1="8" x2="14.5" y2="8"/></svg>
        www.quillnet.example
      </li>
    </ul>

    <p class="address">4/312 Barnaby Parade<br>Kestrel Bay WA 6190, Australia</p>
  </section>
</main>
</body>
</html>
```